Sleep/Snoring Business - Requires Website - Australia

We are seeking a simple to maintain website for our sleep business. The health care business provides diagnostic and treatment solutions for snoring, sleep disorders and other respiratory problems.

Ideally, colours to match the company logo (attached).

The page must be built using WORDPRESS.

Ideally site will have a home page outlining the business, with 5 sub pages - being "Diagnosis" "Treatment Options", "Prodcuts", "About Us", "Contact Us"

The site home page should include a large picture on the home page.

The "Treatment Options" and "Diagnosis" pages must include:
Allow for a few pictures with assocaited text, plus space for some embeded youtube videos.

"Prodcuts" page should have the ability to show 3-4 products across the page with text below.. that can include external URL to products

The "About Us" page must include:
1. a Map (google map) to identify the various locations. There are 6 in total.
2. A Section to describe our doctors/staff - allow for a picture and some text

The "Contact Us" page must include:
email form
telephone details

The overall design should have a clean and medical/safe feeling

Target Market(s)

People who snore and those with sleeping and respiratory disorders

Industry/Entity Type

Health Care

Coding

Coded - Design and coding required

Number of Pages Required

5+ page

Colors

Designer to choose colors to be used in the design.

Requirements
Must have
• The page must be built using WORDPRESS.
• Ideally site will have a home page outlining the business, with 5 sub pages - being "Diagnosis" "Treatment Options", "Prodcuts", "About Us", "Contact Us"
• The site home page should include a large picture on the home page.
• The "Treatment Options" and "Diagnosis" pages must include:
• Allow for a few pictures with assocaited text, plus space for some embeded youtube videos.
• "Prodcuts" page should have the ability to show 3-4 products across the page with text below.. that can include external URL to products
• The "About Us" page must include:
• 1. a Map (google map) to identify the various locations. There are 6 in total.
• 2. A Section to describe our doctors/staff - allow for a picture and some text
• The "Contact Us" page must include:
• email form
• telephone details
• Pictures must be licenced or free to use
Nice to have
• Home page pictures showing people sleeping well, snoring or fresh air (landscape) type transition pictures (at least 3).
Should not have
• Not to look cheap
• This is a high end healthcare business, so must look that way

```html
<!DOCTYPE html>
<html lang="en">
<head>
<meta charset="utf-8">
<title>Somnara Health – Home</title>
<link rel="stylesheet" href="https://fonts.googleapis.com/css2?family=Lato:wght@400;700&family=Marcellus&display=swap">
<style>
  :root {
    --navy: #0f4b7d;
    --navy-deep: #0d4676;
    --sky-blue: #8eaedb;
    --icon-blue: #8fb0dc;
    --text-dark: #333b44;
    --rule: #d6d6d6;
    --white: #ffffff;
  }
  * { box-sizing: border-box; margin: 0; padding: 0; }
  html, body { width: 1200px; height: 894px; overflow: hidden; background: var(--white); }
  body { font-family: "Lato", sans-serif; color: var(--text-dark); position: relative; }

  .site-header { position: absolute; inset: 0 0 auto 0; height: 144px; border-top: 3px solid var(--navy); border-bottom: 1px solid var(--rule); background: var(--white); }
  .brand { position: absolute; left: 52px; top: 38px; display: flex; align-items: center; gap: 12px; }
  .brand-dot { width: 34px; height: 34px; border-radius: 50%; background: var(--navy); }
  .brand-name { font-family: "Lato", sans-serif; font-weight: 700; font-size: 42px; color: var(--navy); letter-spacing: -0.5px; }

  .header-social { position: absolute; top: 22px; left: 790px; display: flex; gap: 13px; }
  .social-ring { width: 34px; height: 34px; border-radius: 50%; border: 1.5px solid var(--icon-blue); }
  .header-divider { position: absolute; left: 961px; top: 22px; width: 1px; height: 36px; background: var(--rule); }
  .header-phone { position: absolute; left: 988px; top: 22px; display: flex; align-items: center; gap: 10px; font-weight: 700; font-size: 17px; color: var(--text-dark); letter-spacing: 0.3px; }
  .phone-ring { width: 33px; height: 33px; border-radius: 50%; border: 1.5px solid var(--icon-blue); display: flex; align-items: center; justify-content: center; }

  .main-nav { position: absolute; top: 94px; right: 54px; display: flex; align-items: center; font-size: 17.5px; }
  .main-nav a { color: var(--text-dark); text-decoration: none; padding: 4px 26px; position: relative; line-height: 22px; }
  .main-nav a + a::before { content: ""; position: absolute; left: 0; top: 4px; width: 1px; height: 20px; background: var(--rule); }
  .main-nav a.is-current { color: var(--navy); border: 1.5px solid var(--navy); border-radius: 16px; padding: 4px 18px; margin-right: 10px; }
  .main-nav a:last-child { padding-right: 0; }

  .hero { position: absolute; top: 144px; left: 0; width: 1200px; height: 600px; overflow: hidden; }
  .hero-photo { position: absolute; inset: 0; background:
      radial-gradient(ellipse at 45% 0%, #ffffff 0%, rgba(255,255,255,0) 45%),
      linear-gradient(180deg, #b9cde3 0%, #dbe6ef 35%, #d9c79a 62%, #b88f4c 85%, #8f6a35 100%); }
  .hero-title { position: absolute; left: 42px; top: 150px; width: 560px; font-family: "Marcellus", serif; font-size: 32px; line-height: 41px; color: var(--navy); }
  .slider-dots { position: absolute; left: 52px; top: 306px; display: flex; gap: 11px; }
  .slider-dots span { width: 14px; height: 14px; border-radius: 50%; background: #9a9a9a; }
  .slider-dots span.is-active { background: var(--navy); border: 2px solid #fff; }
  .hero-wave { position: absolute; inset: 0; }

  .site-footer { position: absolute; top: 740px; left: 0; width: 1200px; height: 154px; background: var(--navy); color: var(--white); }
  .footer-nav { position: absolute; left: 31px; top: 20px; display: flex; font-size: 15px; }
  .footer-nav a { color: var(--white); text-decoration: none; padding: 0 23px; position: relative; line-height: 20px; }
  .footer-nav a + a::before { content: ""; position: absolute; left: 0; top: 1px; width: 1px; height: 18px; background: rgba(255,255,255,0.35); }
  .footer-social { position: absolute; right: 51px; top: 9px; display: flex; gap: 13px; }
  .footer-social .social-ring { border-color: var(--white); }
  .footer-rule { position: absolute; left: 0; right: 0; top: 65px; height: 1px; background: rgba(255,255,255,0.3); }
  .contact-item { position: absolute; top: 89px; display: flex; gap: 22px; font-size: 15px; line-height: 25px; }
  .contact-item svg { margin-top: 6px; flex: none; }
  .contact-item strong { font-weight: 700; display: block; }
  .contact-item .email { font-size: 16.5px; letter-spacing: 0.4px; }
  .copyright { position: absolute; right: 54px; top: 96px; text-align: right; font-size: 14px; line-height: 20px; }
</style>
</head>
<body>
  <header class="site-header">
    <div class="brand">
      <span class="brand-dot"></span>
      <span class="brand-name">Somnara Health</span>
    </div>
    <div class="header-social" aria-label="Social links">
      <span class="social-ring"></span><span class="social-ring"></span><span class="social-ring"></span>
    </div>
    <div class="header-divider"></div>
    <div class="header-phone">
      <span class="phone-ring">
        <svg width="18" height="18" viewBox="0 0 24 24"><path fill="#8fb0dc" d="M6.6 10.8a15 15 0 0 0 6.6 6.6l2.2-2.2c.3-.3.7-.4 1-.2 1.1.4 2.3.6 3.6.6.6 0 1 .4 1 1V20c0 .6-.4 1-1 1A17 17 0 0 1 3 4c0-.6.4-1 1-1h3.5c.6 0 1 .4 1 1 0 1.3.2 2.5.6 3.6.1.3 0 .7-.2 1z"/></svg>
      </span>
      021-555-0147
    </div>
    <nav class="main-nav">
      <a href="#" class="is-current">Home</a>
      <a href="#">Diagnosis</a>
      <a href="#">Treatment</a>
      <a href="#">Products</a>
      <a href="#">About Us</a>
      <a href="#">Contact Us</a>
    </nav>
  </header>

  <section class="hero">
    <div class="hero-photo" role="img" aria-label="Photo of a woman in a green top standing in a golden wheat field with arms raised toward a bright sunlit sky"></div>
    <h1 class="hero-title">We provide diagnostic and treatment solutions for snoring, sleep disorders and other respiratory problems</h1>
    <div class="slider-dots"><span class="is-active"></span><span></span><span></span><span></span></div>
    <svg class="hero-wave" width="1200" height="600" viewBox="0 0 1200 600" aria-hidden="true">
      <path d="M0 486 C 300 610, 850 632, 1200 433 L1200 600 L0 600 Z" fill="#ffffff"/>
      <path d="M0 492 C 300 622, 860 648, 1200 452 L1200 600 L0 600 Z" fill="var(--sky-blue)"/>
      <path d="M0 486 C 260 590, 700 640, 1200 520 L1200 600 L0 600 Z" fill="var(--navy)"/>
    </svg>
  </section>

  <footer class="site-footer">
    <nav class="footer-nav">
      <a href="#">Home</a><a href="#">Diagnosis</a><a href="#">Treatment</a><a href="#">Products</a><a href="#">About Us</a><a href="#">Contact Us</a>
    </nav>
    <div class="footer-social" aria-label="Social links">
      <span class="social-ring"></span><span class="social-ring"></span><span class="social-ring"></span>
    </div>
    <div class="footer-rule"></div>

    <div class="contact-item" style="left:64px">
      <svg width="12" height="17" viewBox="0 0 12 17"><path fill="#fff" d="M6 0a6 6 0 0 0-6 6c0 4.5 6 11 6 11s6-6.5 6-11a6 6 0 0 0-6-6zm0 8.2A2.2 2.2 0 1 1 6 3.8a2.2 2.2 0 0 1 0 4.4z"/></svg>
      <div><strong>Somnara Health</strong>48 Harbour Lane, Bayview North - 204815</div>
    </div>
    <div class="contact-item" style="left:410px">
      <svg width="15" height="15" viewBox="0 0 24 24"><path fill="#fff" d="M6.6 10.8a15 15 0 0 0 6.6 6.6l2.2-2.2c.3-.3.7-.4 1-.2 1.1.4 2.3.6 3.6.6.6 0 1 .4 1 1V20c0 .6-.4 1-1 1A17 17 0 0 1 3 4c0-.6.4-1 1-1h3.5c.6 0 1 .4 1 1 0 1.3.2 2.5.6 3.6.1.3 0 .7-.2 1z"/></svg>
      <div><strong>Call Us :</strong>021-555-0147</div>
    </div>
    <div class="contact-item" style="left:598px">
      <svg width="16" height="12" viewBox="0 0 16 12"><rect width="16" height="12" rx="1" fill="#fff"/><path d="M1 1l7 5.5L15 1" fill="none" stroke="var(--navy)" stroke-width="1.4"/></svg>
      <div><strong>Email Us :</strong><span class="email">info@somnarahealth.com</span></div>
    </div>
    <p class="copyright">© 2017 Somnara Health.<br>All Rights Reserved.</p>
  </footer>
</body>
</html>
```